(draft #51)
please have the below adjustment in your design and they are:
- please change the slide color to become the same color as business card color background.
-#9 the folder inside is not shown kindly try to include if you can.
-please include an A4 Envelope, CD cover, Invoice & Flyer it is very important.
(draft #54)
-in the cd cover please include the address.
-the word oil changing service is needed below each logo.
-in the business card will you enlarge the name and push the address to the right little bit.
-please include an A4 Envelope, Invoice & Flyer it is very important.
(draft #56)
i would like to have some adjustment please and they are:
-in the letter head please will you spread the address horizontally and place it below or at the lower of the letterhead.
-in the Envelope will you take out the phone, fax, mobile and email from the upper side and place it in the lower side.
-in the folder with pocket there is no need for the mobile number and email
-please include an A4 Envelope & Flyer it is very important.
We need data for flyer.
kindly provide it.
please include all stationery like draft 59 and 60.
-please include an A4 Envelope, CD, & Flyer it is very important.
kindly delete the tilted designs logo only the horizontal drops.
but thanks again for your quick action.
thanks again
1- Please include a Folder with 1 or 2 pockets
2- master & theme slides for power point if possible.
i have uploaded the Al and eps files as per your requests and i am hoping to see good designs from you.

```html
<!DOCTYPE html>
<html lang="en">
<head>
<meta charset="utf-8">
<title>motrixa stationery set</title>
<link href="https://fonts.googleapis.com/css2?family=Open+Sans:wght@400;600;700&display=swap" rel="stylesheet">
<style>
:root{
  --orange:#d9531e;
  --orange-dark:#a8300f;
  --gold:#c9a24a;
  --gold-light:#e6cf8f;
  --paper:#ffffff;
  --ink:#444444;
  --muted:#8a8a8a;
  --stage:#e4e4e2;
  --faint:#f3e3dc;
}
*{margin:0;padding:0;box-sizing:border-box}
html,body{width:1200px;height:686px;overflow:hidden}
body{background:var(--stage);font-family:'Open Sans',Arial,sans-serif;color:var(--ink);position:relative}
.item{position:absolute;overflow:hidden;box-shadow:0 2px 6px rgba(0,0,0,.25);background:var(--paper)}
.orange-fill{background:radial-gradient(circle at 70% 40%,#e8672c 0%,var(--orange) 45%,var(--orange-dark) 100%)}
.gold-fill{background:linear-gradient(135deg,var(--gold-light),var(--gold))}
.brand{display:flex;align-items:center;gap:4px;font-weight:700;color:var(--orange);letter-spacing:-.02em}
.brand .dot{border-radius:50%;background:currentColor;flex:none}
.brand.white{color:#fff}
.swoosh{position:absolute;left:0;bottom:0;width:100%}
.swoosh.top{top:0;bottom:auto;transform:scaleY(-1)}
.watermark{position:absolute;border-radius:50%;background:var(--faint);opacity:.7}
.tiny{font-size:4px;line-height:6px;color:var(--muted)}
.contact-row{display:flex;gap:10px;font-size:4px;color:var(--muted)}
.contact-row span::before{content:"";display:inline-block;width:3px;height:3px;border-radius:50%;background:var(--orange);margin-right:2px}

/* business cards */
.card{width:127px;height:72px}
.card-front{left:65px;top:12px}
.card-front .name{position:absolute;left:8px;top:8px;font-size:6px;font-weight:700;color:var(--ink)}
.card-front .role{position:absolute;left:8px;top:15px;font-size:4px;color:var(--muted)}
.card-front .lines{position:absolute;left:8px;top:24px}
.card-front .brand{position:absolute;right:8px;top:36px;font-size:9px}
.card-back{left:199px;top:12px}
.card-gold{left:65px;top:91px}
.card-orange{left:199px;top:91px}
.card .center-brand{position:absolute;left:0;right:0;top:28px;justify-content:center;font-size:11px}

/* sheets */
.sheet{width:208px;height:300px;top:24px}
.letterhead{left:475px}
.invoice{left:703px}
.memo{left:930px}
.sheet .brand{position:absolute;left:14px;top:14px;font-size:12px}
.sheet .head-info{position:absolute;left:88px;top:16px}
.sheet .footer{position:absolute;left:14px;bottom:26px;display:flex;flex-direction:column;gap:3px}
.letterhead .watermark{width:110px;height:110px;left:70px;top:110px}
.invoice-title{position:absolute;left:14px;top:44px;font-size:6px;font-weight:700;color:var(--orange)}
.invoice-table{position:absolute;left:14px;top:58px;width:180px;border-collapse:collapse;font-size:4px}
.invoice-table th{background:var(--orange);color:#fff;padding:2px;font-weight:600;text-align:left}
.invoice-table td{border:0.5px solid #e0b7a4;height:7px;background:#fbeee8}
.invoice-note{position:absolute;left:14px;top:248px;font-size:4px;color:var(--muted)}
.memo-fields{position:absolute;left:14px;top:48px;display:flex;flex-direction:column;gap:6px;width:180px}
.memo-fields div{font-size:4px;color:var(--muted);border-bottom:.5px solid #ccc;padding-bottom:2px}
.memo .watermark{width:100px;height:100px;left:80px;top:120px}

/* slides */
.slide{width:204px;height:156px}
.slide-title{left:36px;top:240px}
.slide-about{left:257px;top:240px}
.slide-thanks{left:36px;top:413px}
.slide-title .brand{position:absolute;left:12px;top:14px;font-size:12px}
.slide-title h2{position:absolute;left:12px;top:96px;font-size:8px;font-weight:700;color:var(--orange)}
.slide-title p{position:absolute;left:12px;top:108px;font-size:5px;color:var(--muted)}
.slide-about h2{position:absolute;left:12px;top:10px;font-size:8px;font-weight:700;color:var(--orange)}
.slide-thanks .brand{position:absolute;left:12px;top:14px;font-size:12px}
.slide-thanks h2{position:absolute;left:12px;top:104px;font-size:6px;font-weight:700;color:#fff}
.slide-thanks p{position:absolute;left:12px;top:113px;font-size:4px;color:#fde2d4}

/* envelopes */
.envelope{width:208px;height:80px;top:350px}
.env-front{left:475px}
.env-back{left:703px}
.env-open{left:930px;width:217px}
.env-front .brand{position:absolute;left:10px;top:8px;font-size:9px}
.env-front .contact-row{position:absolute;left:10px;bottom:6px}

/* cd */
.cd-disc{position:absolute;left:278px;top:426px;width:114px;height:114px;border-radius:50%;box-shadow:0 2px 6px rgba(0,0,0,.25);overflow:hidden;background:var(--paper)}
.cd-disc .hole{position:absolute;left:45px;top:45px;width:24px;height:24px;border-radius:50%;background:var(--stage);border:4px solid #ddd}
.cd-disc .brand{position:absolute;left:20px;top:22px;font-size:9px}
.cd-cover{left:276px;top:516px;width:180px;height:156px}
.cd-cover .brand{position:absolute;left:10px;top:60px;font-size:12px}
.cd-cover .tiny{position:absolute;left:10px;top:78px}

/* folders */
.folder-open{left:456px;top:444px;width:336px;height:228px}
.folder-open .pocket-left{position:absolute;left:0;bottom:0;width:168px;height:56px}
.folder-open .pocket-right{position:absolute;right:0;bottom:0;width:168px;height:56px}
.folder-open .pocket-right .brand{position:absolute;right:12px;top:20px;font-size:10px}
.folder-open .watermark{width:120px;height:120px;left:190px;top:20px}
.folder-closed{left:804px;top:444px;width:348px;height:228px;display:flex}
.folder-closed .back-panel{width:50%;position:relative}
.folder-closed .front-panel{width:50%;position:relative;border-left:1px solid rgba(0,0,0,.15)}
.folder-closed .front-panel .brand{position:absolute;left:24px;top:96px;font-size:14px}
.folder-closed .back-panel .tiny{position:absolute;left:14px;bottom:14px;color:#fde2d4}
</style>
</head>
<body>

<!-- Business cards -->
<div class="item card card-front">
  <div class="name">Eng. Omar K. Haddad</div>
  <div class="role">General Manager</div>
  <div class="lines tiny">Tel 011 234 5678<br>info@motrixa.com</div>
  <div class="brand"><span class="dot" style="width:6px;height:6px"></span>motrixa</div>
  <svg class="swoosh" viewBox="0 0 200 30" preserveAspectRatio="none" height="12"><path d="M0 30 L0 22 Q100 6 200 14 L200 30Z" fill="var(--gold)"/><path d="M0 30 L0 26 Q100 12 200 20 L200 30Z" fill="var(--orange)"/></svg>
</div>
<div class="item card card-back orange-fill">
  <div class="brand white center-brand"><span class="dot" style="width:7px;height:7px"></span>motrixa</div>
</div>
<div class="item card card-gold gold-fill">
  <div class="brand white center-brand"><span class="dot" style="width:7px;height:7px"></span>motrixa</div>
</div>
<div class="item card card-orange orange-fill">
  <div class="brand white center-brand"><span class="dot" style="width:7px;height:7px"></span>motrixa</div>
</div>

<!-- Letterhead -->
<div class="item sheet letterhead">
  <div class="brand"><span class="dot" style="width:8px;height:8px"></span>motrixa</div>
  <div class="head-info tiny">Tel 011 234 5678 | Fax 011 234 5679</div>
  <div class="watermark"></div>
  <div class="footer">
    <div class="contact-row"><span>P.O. Box 1020, Riyadh 11431</span></div>
    <div class="contact-row"><span>Tel 011 234 5678</span></div>
    <div class="contact-row"><span>www.motrixa.com</span></div>
  </div>
  <svg class="swoosh" viewBox="0 0 200 30" preserveAspectRatio="none" height="20"><path d="M0 30 L0 18 Q110 4 200 12 L200 30Z" fill="var(--gold)"/><path d="M0 30 L0 24 Q110 10 200 18 L200 30Z" fill="var(--orange)"/></svg>
</div>

<!-- Invoice -->
<div class="item sheet invoice">
  <div class="brand"><span class="dot" style="width:8px;height:8px"></span>motrixa</div>
  <div class="invoice-title">INVOICE</div>
  <table class="invoice-table">
    <tr><th>Item</th><th>Description</th><th>Qty</th><th>Price</th><th>Total</th></tr>
    <tr><td></td><td></td><td></td><td></td><td></td></tr>
    <tr><td></td><td></td><td></td><td></td><td></td></tr>
    <tr><td></td><td></td><td></td><td></td><td></td></tr>
    <tr><td></td><td></td><td></td><td></td><td></td></tr>
    <tr><td></td><td></td><td></td><td></td><td></td></tr>
    <tr><td></td><td></td><td></td><td></td><td></td></tr>
    <tr><td></td><td></td><td></td><td></td><td></td></tr>
    <tr><td></td><td></td><td></td><td></td><td></td></tr>
    <tr><td></td><td></td><td></td><td></td><td></td></tr>
    <tr><td></td><td></td><td></td><td></td><td></td></tr>
    <tr><td></td><td></td><td></td><td></td><td></td></tr>
    <tr><td></td><td></td><td></td><td></td><td></td></tr>
    <tr><td></td><td></td><td></td><td></td><td></td></tr>
    <tr><td></td><td></td><td></td><td></td><td></td></tr>
    <tr><td></td><td></td><td></td><td></td><td></td></tr>
    <tr><td></td><td></td><td></td><td></td><td></td></tr>
    <tr><td></td><td></td><td></td><td></td><td></td></tr>
    <tr><td></td><td></td><td></td><td></td><td></td></tr>
    <tr><td></td><td></td><td></td><td></td><td></td></tr>
    <tr><td></td><td></td><td></td><td></td><td></td></tr>
  </table>
  <div class="invoice-note">Thank you for your business</div>
  <svg class="swoosh" viewBox="0 0 200 30" preserveAspectRatio="none" height="20"><path d="M0 30 L0 18 Q110 4 200 12 L200 30Z" fill="var(--gold)"/><path d="M0 30 L0 24 Q110 10 200 18 L200 30Z" fill="var(--orange)"/></svg>
</div>

<!-- Memo / fax sheet -->
<div class="item sheet memo">
  <div class="brand"><span class="dot" style="width:8px;height:8px"></span>motrixa</div>
  <div class="memo-fields"><div>To:</div><div>From:</div><div>Date:</div><div>Subject:</div></div>
  <div class="watermark"></div>
  <div class="footer">
    <div class="contact-row"><span>P.O. Box 1020, Riyadh 11431</span></div>
    <div class="contact-row"><span>Tel 011 234 5678</span></div>
    <div class="contact-row"><span>www.motrixa.com</span></div>
  </div>
  <svg class="swoosh" viewBox="0 0 200 30" preserveAspectRatio="none" height="20"><path d="M0 30 L0 18 Q110 4 200 12 L200 30Z" fill="var(--gold)"/><path d="M0 30 L0 24 Q110 10 200 18 L200 30Z" fill="var(--orange)"/></svg>
</div>

<!-- Slides -->
<div class="item slide slide-title">
  <div class="brand"><span class="dot" style="width:8px;height:8px"></span>motrixa</div>
  <h2>YOUR TITLE GOES HERE</h2>
  <p>Company Name</p>
  <svg class="swoosh" viewBox="0 0 200 30" preserveAspectRatio="none" height="22"><path d="M0 30 L0 16 Q120 2 200 10 L200 30Z" fill="var(--gold)"/><path d="M0 30 L0 22 Q120 8 200 16 L200 30Z" fill="var(--orange)"/></svg>
</div>
<div class="item slide slide-about">
  <svg class="swoosh top" viewBox="0 0 200 30" preserveAspectRatio="none" height="28"><path d="M0 30 L0 16 Q120 2 200 10 L200 30Z" fill="var(--gold)"/><path d="M0 30 L0 22 Q120 8 200 16 L200 30Z" fill="var(--orange)"/></svg>
  <h2 style="top:32px">ABOUT US</h2>
  <svg class="swoosh" viewBox="0 0 200 30" preserveAspectRatio="none" height="14"><path d="M0 30 L0 18 Q120 4 200 12 L200 30Z" fill="var(--gold)"/><path d="M0 30 L0 24 Q120 10 200 18 L200 30Z" fill="var(--orange)"/></svg>
</div>
<div class="item slide slide-thanks orange-fill">
  <div class="brand white"><span class="dot" style="width:8px;height:8px"></span>motrixa</div>
  <h2>THANK YOU FOR YOUR ATTENTION</h2>
  <p>PRODUCTS</p>
</div>

<!-- Envelopes -->
<div class="item envelope env-front">
  <div class="brand"><span class="dot" style="width:6px;height:6px"></span>motrixa</div>
  <div class="contact-row"><span>Tel 011 234 5678</span><span>www.motrixa.com</span></div>
  <svg class="swoosh" viewBox="0 0 200 30" preserveAspectRatio="none" height="12"><path d="M0 30 L0 18 Q110 4 200 12 L200 30Z" fill="var(--gold)"/><path d="M0 30 L0 24 Q110 10 200 18 L200 30Z" fill="var(--orange)"/></svg>
</div>
<div class="item envelope env-back">
  <svg width="100%" height="100%" viewBox="0 0 208 80" preserveAspectRatio="none"><path d="M0 0 H208 V20 L104 52 L0 20Z" fill="var(--orange)"/><path d="M0 20 L104 52 L208 20" stroke="var(--gold)" stroke-width="1.5" fill="none"/></svg>
</div>
<div class="item envelope env-open">
  <svg width="100%" height="100%" viewBox="0 0 217 80" preserveAspectRatio="none"><path d="M0 0 H217 V18 L108 46 L0 18Z" fill="var(--orange)"/><path d="M0 80 L108 40 L217 80" stroke="#e2e2e2" stroke-width="1" fill="none"/></svg>
</div>

<!-- CD -->
<div class="item cd-cover">
  <div class="brand"><span class="dot" style="width:8px;height:8px"></span>motrixa</div>
  <div class="tiny">P.O. Box 1020, Riyadh</div>
  <svg class="swoosh" viewBox="0 0 200 30" preserveAspectRatio="none" height="22"><path d="M0 30 L0 16 Q120 2 200 10 L200 30Z" fill="var(--gold)"/><path d="M0 30 L0 22 Q120 8 200 16 L200 30Z" fill="var(--orange)"/></svg>
</div>
<div class="cd-disc">
  <svg class="swoosh" viewBox="0 0 100 40" preserveAspectRatio="none" height="46"><path d="M0 40 L0 14 Q50 0 100 10 L100 40Z" fill="var(--orange)"/><path d="M0 14 Q50 0 100 10" stroke="var(--gold)" stroke-width="2" fill="none"/></svg>
  <div class="brand"><span class="dot" style="width:6px;height:6px"></span>motrixa</div>
  <div class="hole"></div>
</div>

<!-- Folders -->
<div class="item folder-open">
  <div class="watermark"></div>
  <div class="pocket-left gold-fill"></div>
  <div class="pocket-right orange-fill">
    <div class="brand white"><span class="dot" style="width:7px;height:7px"></span>motrixa</div>
  </div>
</div>
<div class="item folder-closed">
  <div class="back-panel orange-fill"><div class="tiny">www.motrixa.com</div></div>
  <div class="front-panel orange-fill">
    <div class="brand white"><span class="dot" style="width:9px;height:9px"></span>motrixa</div>
  </div>
</div>

</body>
</html>
```